I need a wordpress website for myconsulting company specialized in data privacy

I'm looking for a wordpress website for my consulting company specialized in data privacy (GDPR) and computer science.
The website will serve as entry point to for potential clients.
The website should have the following sections (I'm opened to new ideas):
- Presentation of the company
- General presentation
- Services provided with some details
- Blog/articles with tags (if possible)
- Contact
On every page of the website there should be some references to pages (such as privacy policy, legal information...)
If possible he website should be multinlingual (english and french). I'll personnally take care of the translation in french.
Regarding branding;
- Name of the company: Laurent Dubreuil Conseil
- Logo is attached
- For colors to be used see attached PDF for exemple

```html
<!DOCTYPE html>
<html lang="en">
<head>
<meta charset="utf-8">
<title>Laurent Dubreuil Conseil — Data Privacy &amp; Computer Science Consultancy</title>
<link href="https://fonts.googleapis.com/css2?family=Michroma&family=Nunito+Sans:wght@400;600;700&display=swap" rel="stylesheet">
<style>
:root{
  --teal:#0aa0ad;
  --teal-dark:#078593;
  --navy:#0b3a52;
  --ink:#062c40;
  --text:#2b2b2b;
  --muted:#555;
  --grey-bg:#f3f3f3;
  --line:#d9d9d9;
  --white:#fff;
}
*{box-sizing:border-box;margin:0;padding:0}
html,body{width:1200px;height:2962px;overflow:hidden}
body{position:relative;background:var(--white);font-family:"Nunito Sans",sans-serif;color:var(--text)}
.abs{position:absolute}
.display{font-family:"Michroma",sans-serif;font-weight:400}
.btn{position:absolute;background:var(--teal);color:var(--white);font-family:"Michroma",sans-serif;font-size:13px;letter-spacing:.5px;display:flex;align-items:center;justify-content:center;text-decoration:none}

/* header */
.site-header{position:absolute;left:0;top:0;width:1200px;height:101px;background:var(--white)}
.brand{position:absolute;text-align:center;color:var(--navy)}
.brand .mark{width:26px;height:26px;background:var(--teal);margin:0 auto 6px}
.brand .name{font-family:"Michroma",sans-serif;font-size:15px;white-space:nowrap}
.brand .sub{font-size:8px;letter-spacing:7px;color:var(--teal);display:flex;align-items:center;justify-content:center;gap:6px;margin-top:2px}
.brand .sub::before,.brand .sub::after{content:"";width:30px;height:1px;background:var(--teal)}
.main-nav a{position:absolute;top:42px;font-size:14px;color:#333;text-decoration:none}
.main-nav a.active::after{content:"";position:absolute;left:0;right:0;top:22px;height:1px;background:var(--teal)}
.lang{position:absolute;left:986px;top:34px;width:53px;height:33px;background:var(--teal);color:var(--white);font-size:14px;display:flex;align-items:center;justify-content:center;gap:6px}

/* hero */
.hero{position:absolute;left:0;top:101px;width:1200px;height:569px}
.hero h1{position:absolute;left:0;top:196px;width:1200px;text-align:center;color:var(--white);font-size:33px;line-height:41px;letter-spacing:1px}

/* about */
.about-frame-a{position:absolute;left:161px;top:758px;width:120px;height:110px;border-left:4px solid var(--teal);border-top:4px solid var(--teal)}
.about-frame-b{position:absolute;left:353px;top:952px;width:147px;height:145px;border-right:5px solid var(--ink);border-bottom:5px solid var(--ink)}
.about-photo{position:absolute;left:176px;top:773px;width:309px;height:309px;background:radial-gradient(circle at 50% 45%,#1fa9cf,#0b6f9c 55%,#075179)}
.about-photo span{position:absolute;bottom:18px;left:0;right:0;text-align:center;color:#dff6ff;font-family:"Michroma",sans-serif;font-size:14px}
.about-title{position:absolute;left:601px;top:752px;color:var(--teal);font-size:32px}
.about-name{position:absolute;left:600px;top:790px;color:var(--navy);font-size:34px;white-space:nowrap}
.about-sub{position:absolute;left:602px;top:830px;width:392px;display:flex;align-items:center;gap:14px;color:var(--teal);font-size:12px;letter-spacing:17px;font-family:"Michroma",sans-serif}
.about-sub::before,.about-sub::after{content:"";flex:1;height:1px;background:var(--teal)}
.about-text{position:absolute;left:601px;top:870px;width:390px;font-size:13.5px;line-height:24.5px;color:var(--text)}
.about-text p+p{margin-top:6px}

/* section titles */
.section-title{position:absolute;left:0;width:1200px;text-align:center;font-size:32px;color:var(--navy)}
.section-title .accent{color:var(--teal)}
.section-rule{position:absolute;left:550px;width:100px;height:10px;display:flex;align-items:center;gap:8px}
.section-rule::before,.section-rule::after{content:"";flex:1;height:1px;background:var(--teal)}
.section-rule i{width:7px;height:7px;background:var(--navy)}

/* services */
.services{position:absolute;left:0;top:1183px;width:1200px;height:543px;background:var(--grey-bg)}
.service h3{position:absolute;left:160px;font-family:"Michroma",sans-serif;font-size:14.5px;color:#111;white-space:nowrap}
.service p{position:absolute;left:160px;width:310px;font-size:13.5px;line-height:25px;color:var(--text)}
.hub{position:absolute;left:761px;top:1358px;width:278px;height:278px;border-radius:50%;background:var(--white);display:flex;flex-direction:column;align-items:center;justify-content:center;color:var(--navy)}
.hub .mark{width:60px;height:60px;background:var(--teal);margin-bottom:14px}
.hub .name{font-family:"Michroma",sans-serif;font-size:15px}

/* blog */
.blog-grid{position:absolute;left:161px;top:1899px;width:878px;height:313px;border:1px solid var(--line)}
.post{position:absolute;width:439px;height:156px;border-color:var(--line)}
.post .thumb{position:absolute;left:24px;top:41px;width:74px;height:74px;border-radius:50%}
.post time{position:absolute;left:118px;top:46px;font-size:12px;color:#333}
.post h4{position:absolute;left:118px;top:72px;width:305px;font-family:"Michroma",sans-serif;font-size:12.3px;line-height:18px;color:#111;font-weight:400}
.post.featured{box-shadow:0 0 12px rgba(0,0,0,.09);background:var(--white)}
.post.featured h4{color:var(--teal)}

/* clients */
.client{position:absolute;top:2475px;height:40px;display:flex;align-items:center;gap:8px;font-family:"Nunito Sans",sans-serif;font-weight:700;font-size:29px;color:#b7b7b7;transform:translateX(-50%)}
.client i{width:30px;height:30px;border-radius:50%;background:#c8c8c8}
.client.active{color:var(--navy)}
.client.active i{background:var(--teal)}
.client-box{position:absolute;left:524px;top:2465px;width:149px;height:55px;background:var(--white);box-shadow:0 2px 12px rgba(0,0,0,.12)}
.arrow{position:absolute;top:2473px;width:39px;height:39px;border-radius:50%;display:flex;align-items:center;justify-content:center;font-size:20px}

/* footer */
.footer-bg{position:absolute;left:0;top:2612px;width:1200px;height:350px}
.f-icon{position:absolute;width:38px;height:38px;border-radius:50%;border:1px solid rgba(255,255,255,.45);display:flex;align-items:center;justify-content:center}
.f-label{position:absolute;color:var(--white);font-size:13.5px;line-height:21px}
.f-label b{font-weight:700}
.f-name{position:absolute;left:208px;top:2733px;color:var(--white);font-family:"Michroma",sans-serif;font-size:20px;white-space:nowrap}
.f-brand{position:absolute;left:804px;top:2718px;width:240px;text-align:center;color:var(--white)}
.f-brand .mark{width:30px;height:30px;background:var(--teal);margin:0 auto 6px}
.f-brand .name{font-family:"Michroma",sans-serif;font-size:15px}
.f-brand .sub{font-size:7px;letter-spacing:7px;color:var(--teal)}
.f-brand p{font-size:13.5px;line-height:21px;margin-top:8px}
.f-rule{position:absolute;left:161px;top:2869px;width:878px;height:1px;background:rgba(255,255,255,.25)}
.f-nav a{position:absolute;top:2903px;color:var(--white);font-size:13.5px;text-decoration:none}
.f-nav a.active{font-weight:700}
.social{position:absolute;top:2898px;width:30px;height:30px;border-radius:50%;border:1.5px solid var(--white)}
.social.active{background:var(--white)}
.f-legal{position:absolute;left:813px;top:2903px;color:var(--white);font-size:13.5px}
.f-strip{position:absolute;left:0;top:2955px;width:1200px;height:7px;background:var(--teal)}
</style>
</head>
<body>

<header class="site-header">
  <div class="brand" style="left:161px;top:14px;width:189px">
    <div class="mark"></div>
    <div class="name">Laurent Dubreuil</div>
    <div class="sub">CONSEIL</div>
  </div>
  <nav class="main-nav">
    <a class="active" href="#" style="left:631px">Home</a>
    <a href="#" style="left:708px">Services</a>
    <a href="#" style="left:800px">Blogs</a>
    <a href="#" style="left:874px">Contact Us</a>
  </nav>
  <div class="lang">En
    <svg width="10" height="7" viewBox="0 0 10 7"><path d="M1 1l4 4 4-4" fill="none" stroke="#fff" stroke-width="1.5"/></svg>
  </div>
</header>

<section class="hero">
  <svg class="abs" style="left:0;top:0" width="1200" height="569" viewBox="0 0 1200 569">
    <defs>
      <radialGradient id="heroGlow" cx="50%" cy="45%" r="70%">
        <stop offset="0" stop-color="#1e6f92"/>
        <stop offset=".55" stop-color="#0d4766"/>
        <stop offset="1" stop-color="#072a40"/>
      </radialGradient>
    </defs>
    <polygon points="0,0 1200,0 1200,487 600,569 0,487" fill="#0aa0ad"/>
    <polygon points="0,0 1200,0 1200,487 600,561 0,487" fill="#0b3a52"/>
    <rect x="0" y="0" width="1200" height="487" fill="url(#heroGlow)" role="img" aria-label="Digital security background with network icons and a padlock"/>
    <polygon points="0,487 600,561 1200,487" fill="#0e4868"/>
  </svg>
  <h1 class="display">We Specialize In Data Privacy (GDPR)<br>&amp; Computer Science Consultancy</h1>
  <a class="btn" href="#" style="left:520px;top:290px;width:159px;height:44px">CONTACT US</a>
</section>

<section class="about">
  <div class="about-frame-a"></div>
  <div class="about-frame-b"></div>
  <div class="about-photo" role="img" aria-label="Circuit-board padlock illustration for data privacy"><span>DATA PRIVACY</span></div>
  <h2 class="about-title display">About</h2>
  <div class="about-name display">Laurent Dubreuil</div>
  <div class="about-sub">CONSEIL</div>
  <div class="about-text">
    <p>Lorem ipsum dolor sit amet, consectetur adipiscing elit. Praesent eget mi erat. Vivamus neque augue.</p>
    <p>Posuere nec posuere eget, mattis ut tortor. Ut porttitor maximus augue vel congue. Vivamus euismod lectus in libero auctor consectetur. Nunc odio lorem, ornare sit amet elit sit amet, laoreet euismod justo.</p>
  </div>
  <a class="btn" href="#" style="left:600px;top:1051px;width:159px;height:45px">CONTACT US</a>
</section>

<section class="services">
</section>
<h2 class="section-title display" style="top:1266px"><span class="accent">Our</span> Services</h2>
<div class="section-rule" style="top:1312px"><i></i></div>

<div class="service">
  <h3 style="top:1406px">Data Privacy (GDPR) Consultancy</h3>
  <p style="top:1427px">Lorem ipsum dolor sit amet, consectetur adip iscing elit. Praesent eget mi erat.</p>
</div>
<div class="service">
  <h3 style="top:1541px">Computer Science Consultancy</h3>
  <p style="top:1562px">Lorem ipsum dolor sit amet, consectetur adip iscing elit. Praesent eget mi erat.</p>
</div>

<svg class="abs" style="left:490px;top:1390px" width="270" height="240" viewBox="0 0 270 240">
  <circle cx="51" cy="50" r="42" fill="#fff"/>
  <circle cx="51" cy="50" r="36" fill="#0aa0ad"/>
  <rect x="38" y="37" width="26" height="20" rx="2" fill="none" stroke="#fff" stroke-width="2"/>
  <rect x="45" y="44" width="12" height="10" fill="none" stroke="#fff" stroke-width="1.8"/>
  <path d="M47 44v-3a4 4 0 0 1 8 0v3" fill="none" stroke="#fff" stroke-width="1.8"/>
  <path d="M34 60h34" stroke="#fff" stroke-width="2"/>
  <circle cx="51" cy="184" r="42" fill="#fff"/>
  <circle cx="51" cy="184" r="36" fill="#062c40"/>
  <rect x="37" y="170" width="28" height="20" rx="2" fill="none" stroke="#fff" stroke-width="2"/>
  <circle cx="51" cy="180" r="5" fill="none" stroke="#fff" stroke-width="1.8"/>
  <path d="M45 196h12M51 190v6" stroke="#fff" stroke-width="2"/>
  <path d="M115 55v22a12 12 0 0 0 12 12h112" fill="none" stroke="#062c40" stroke-width="3"/>
  <circle cx="115" cy="52" r="5" fill="#062c40"/>
  <circle cx="249" cy="89" r="6" fill="#0aa0ad"/>
  <path d="M115 180v-15a12 12 0 0 1 12-12h112" fill="none" stroke="#062c40" stroke-width="3"/>
  <circle cx="115" cy="183" r="5" fill="#062c40"/>
  <circle cx="249" cy="153" r="6" fill="#0aa0ad"/>
</svg>
<div class="hub"><div class="mark"></div><div class="name">Laurent Dubreuil</div></div>

<h2 class="section-title display" style="top:1810px"><span class="accent">Blog</span> Posts</h2>
<div class="section-rule" style="top:1856px"><i></i></div>

<div class="blog-grid">
  <svg class="abs" style="left:0;top:0" width="878" height="313"><path d="M438.5 0v313M0 156.5h878" stroke="#d9d9d9"/></svg>
  <article class="post featured" style="left:-1px;top:-1px">
    <div class="thumb" role="img" aria-label="Circuit board photo" style="background:radial-gradient(circle,#2a9b8e,#0c3b3a)"></div>
    <time>Feb 20, 2022</time>
    <h4>Lorem ipsum dolor sit amet, cons ectetur adip iscing elit Praesent.</h4>
  </article>
  <article class="post" style="left:439px;top:0">
    <div class="thumb" role="img" aria-label="Laptop showing analytics dashboard" style="background:radial-gradient(circle,#9aa7b4,#2d3a48)"></div>
    <time>Feb 18, 2022</time>
    <h4>Lorem ipsum dolor sit amet, cons ectetur adip iscing elit Praesent.</h4>
  </article>
  <article class="post" style="left:0;top:157px">
    <div class="thumb" role="img" aria-label="Person working with a tablet" style="background:radial-gradient(circle,#e4e8ee,#9eb0c4)"></div>
    <time>Feb 16, 2022</time>
    <h4>Lorem ipsum dolor sit amet, cons ectetur adip iscing elit Praesent.</h4>
  </article>
  <article class="post" style="left:439px;top:157px">
    <div class="thumb" role="img" aria-label="Hand holding a smartphone" style="background:radial-gradient(circle,#c0504a,#0e3d5a 65%)"></div>
    <time>Feb 10, 2022</time>
    <h4>Lorem ipsum dolor sit amet, cons ectetur adip iscing elit Praesent.</h4>
  </article>
</div>
<a class="btn" href="#" style="left:520px;top:2250px;width:159px;height:44px">VIEW ALL</a>

<h2 class="section-title display" style="top:2376px"><span class="accent">Our</span> Clients</h2>
<div class="section-rule" style="top:2422px"><i></i></div>

<div class="arrow" style="left:122px;border:1.5px solid var(--teal);color:var(--teal)">&#8592;</div>
<div class="client-box"></div>
<div class="client" style="left:248px"><i></i>Brixel</div>
<div class="client" style="left:423px"><i></i>Norvan</div>
<div class="client active" style="left:598px"><i></i>Solen</div>
<div class="client" style="left:773px"><i></i>Quadra</div>
<div class="client" style="left:949px"><i></i>Orbit</div>
<div class="arrow" style="left:1038px;background:var(--teal);color:#fff">&#8594;</div>

<footer>
  <svg class="footer-bg" width="1200" height="350" viewBox="0 0 1200 350">
    <defs>
      <linearGradient id="footGrad" x1="0" y1="0" x2="0" y2="1">
        <stop offset="0" stop-color="#0b3a5a"/>
        <stop offset="1" stop-color="#0a5578"/>
      </linearGradient>
    </defs>
    <polygon points="0,48 600,0 1200,48 1200,350 0,350" fill="url(#footGrad)"/>
  </svg>

  <div class="f-icon" style="left:161px;top:2727px">
    <svg width="14" height="18" viewBox="0 0 14 18"><path d="M7 1a6 6 0 0 0-6 6c0 4.5 6 10 6 10s6-5.5 6-10a6 6 0 0 0-6-6z" fill="none" stroke="#0aa0ad" stroke-width="1.6"/><circle cx="7" cy="7" r="2" fill="#0aa0ad"/></svg>
  </div>
  <div class="f-name">Laurent Dubreuil</div>
  <div class="f-label" style="left:209px;top:2772px">123 Building Name, Street Name,<br>City Name, State XY-123456</div>

  <div class="f-icon" style="left:496px;top:2727px">
    <svg width="16" height="16" viewBox="0 0 16 16"><path d="M3 1.5l3 3-1.6 2a9 9 0 0 0 5 5l2-1.6 3 3-2 2C7 14.5 1.5 9 1 3.5z" fill="#0aa0ad"/></svg>
  </div>
  <div class="f-label" style="left:547px;top:2725px"><b>Phone</b><br>123 456 7890</div>

  <div class="f-icon" style="left:496px;top:2787px">
    <svg width="16" height="12" viewBox="0 0 16 12"><rect x="0" y="0" width="16" height="12" rx="1.5" fill="#0aa0ad"/><path d="M1 1l7 5 7-5" fill="none" stroke="#0b3a5a" stroke-width="1.4"/></svg>
  </div>
  <div class="f-label" style="left:547px;top:2785px"><b>Email</b><br>info@laurentdubreuil-conseil.com</div>

  <div class="f-brand">
    <div class="mark"></div>
    <div class="name">Laurent Dubreuil</div>
    <div class="sub">CONSEIL</div>
    <p>Copyright © 2022 Laurent Dubreuil.<br>All Rights Reserved.</p>
  </div>

  <div class="f-rule"></div>
  <nav class="f-nav">
    <a class="active" href="#" style="left:163px">Home</a>
    <a href="#" style="left:232px">Services</a>
    <a href="#" style="left:315px">Blogs</a>
    <a href="#" style="left:380px">Contact Us</a>
  </nav>
  <a class="social active" href="#" aria-label="Social profile 1" style="left:526px"></a>
  <a class="social" href="#" aria-label="Social profile 2" style="left:565px"></a>
  <a class="social" href="#" aria-label="Social profile 3" style="left:604px"></a>
  <a class="social" href="#" aria-label="Social profile 4" style="left:642px"></a>
  <div class="f-legal">Privacy Policy | Terms &amp; Conditions</div>
  <div class="f-strip"></div>
</footer>

</body>
</html>
```